Business card design needed

Family General Practitioner/ Family Physician.
Logo is the logo of the Crestmoor Guild of Family Clinicians Australia
http://kvplm.tarevo.edu.au/PictureGallery/logos/pages/CGFC%20logo_jpg.htm

Reason: Just a bit more time to make changes and the weekend for me to look at things closely and to choose. Thanks, Lumi

Thanks for all the submissions. So many of them are really works of art. Not one of them are not good. The ones that I am eliminating are the ones that I think are not suitable for me personally only, and because if I don't, it makes it very difficult to decide as many of you are also sending me slight variations of a card. I have just decided to choose a second place card too. Can't thank you all enough. Good luck, Lumi. P.S - Working today till 10 pm as the card says :-), so probably won't be able to give a feedback till late Saturday night or Sunday morning here in Sydney, Australia. 

Reason: Just added a second place to the budget and realised that Australia is ahead of the rest of the world in the time zone (only :-) - don't want to offend anyone or start a debate!! ) , so Monday deadline will mean it will be a weekend for the rest of the world. Just wanted to give everyone more time to submit their best, especially since I will be picking a second card too. Can't thank everyone enough for the submissions. P.S - Not keen on photos on the card.

Contact Information for Business Card

Dr. Lumi Harcourt M.B.B.S., F.C.G.F.C
Family General Practitioner
Address, timings, phone and fax number on the back.

Requirements
Must have
• Timings
Mon 7 am - 7 pm
Tues 7 am - 12 pm
Wed 7 am - 10 pm
Thurs 7 am - 12 pm
Fri 7 am - 8 pm
Sat 8 am - 10 pm
Sun - Off

```html
<!DOCTYPE html>
<html lang="en">
<head>
<meta charset="utf-8">
<title>Dr. Lumi Harcourt – Business Card</title>
<link rel="stylesheet" href="https://fonts.googleapis.com/css2?family=Tinos:wght@400;700&family=Source+Sans+3:ital,wght@0,400;1,700&display=swap">
<style>
  :root{
    --bg:#e7e4e0;
    --navy-light:#33608f;
    --navy:#234670;
    --navy-dark:#1a3354;
    --red:#a61d22;
    --red-dark:#7a1a1c;
    --gold:#c9a45c;
    --white:#ffffff;
    --ink:#4a4a4a;
    --ink-dark:#333333;
    --grey-line:#b9bcc2;
  }
  *{margin:0;padding:0;box-sizing:border-box}
  html,body{width:1200px;height:734px;overflow:hidden;background:var(--bg)}
  .canvas{position:relative;width:1200px;height:734px}

  .card{position:absolute;width:543px;height:310px;overflow:hidden;box-shadow:0 3px 10px rgba(0,0,0,.25)}
  .card--front{left:275px;top:36px;background:radial-gradient(ellipse at 50% 45%,var(--navy-light),var(--navy) 55%,var(--navy-dark))}
  .card--back-navy{left:45px;top:379px;background:radial-gradient(ellipse at 45% 40%,var(--navy-light),var(--navy) 55%,var(--navy-dark))}
  .card--back-white{left:622px;top:379px;background:var(--white)}

  .serif{font-family:"Tinos","Times New Roman",serif}
  .sans{font-family:"Source Sans 3","Myriad Pro",sans-serif}

  .front-text{position:absolute;left:0;width:500px;text-align:center;color:var(--white)}
  .doctor-name{top:18px;font-size:34px;font-weight:700;letter-spacing:1.5px}
  .credentials{top:62px;font-size:12px;letter-spacing:.5px}
  .role{top:98px;font-size:18px;letter-spacing:1.2px}
  .address{top:142px;font-size:13.5px;line-height:19px}
  .phones{top:190px;font-size:18px;letter-spacing:1px;display:flex;justify-content:center;gap:12px;align-items:center}
  .phones svg{width:15px;height:15px;vertical-align:-2px;margin-right:5px}
  .tagline{top:270px;width:543px;font-size:20px;letter-spacing:1.8px}

  .wave{position:absolute;left:0;top:0;width:543px;height:310px}

  .guild-mark{position:absolute;left:428px;top:20px;width:104px;height:80px;display:flex;flex-direction:column;align-items:center;justify-content:center;gap:6px;color:var(--white);font-family:"Tinos","Times New Roman",serif;font-size:22px;font-weight:700}
  .guild-mark .dot{width:36px;height:36px;border-radius:50%;background:var(--gold)}

  .guild-ghost{position:absolute;font-family:"Tinos","Times New Roman",serif;font-weight:700;font-size:80px;letter-spacing:4px;pointer-events:none}
  .card--back-navy .guild-ghost{left:150px;top:95px;color:rgba(255,255,255,.06)}
  .card--back-white .guild-ghost{left:150px;top:100px;color:rgba(0,0,0,.05)}

  .hours{position:absolute;font-family:"Source Sans 3","Myriad Pro",sans-serif}
  .hours h2{font-weight:400;font-size:21px;line-height:26px;margin-bottom:2px}
  .hours li{list-style:none;font-size:17px;line-height:21.6px;white-space:pre}
  .card--back-navy .hours{left:40px;top:26px;color:var(--white)}
  .card--back-white .hours{left:16px;top:72px;color:var(--ink)}
  .card--back-white .hours h2{color:var(--red)}

  .divider{position:absolute;width:2px}
  .card--back-navy .divider{left:253px;top:20px;height:180px;background:linear-gradient(to bottom,transparent,rgba(255,255,255,.8) 40%,transparent)}
  .card--back-white .divider{left:221px;top:60px;height:175px;background:linear-gradient(to bottom,transparent,#8d8d8d 40%,transparent)}

  .appointment{position:absolute;font-family:"Source Sans 3","Myriad Pro",sans-serif;width:236px}
  .appointment h3{font-style:italic;font-weight:700;font-size:19px;line-height:24px;margin-bottom:20px}
  .field{display:flex;align-items:flex-end;font-size:19px;line-height:24px;margin-bottom:22px}
  .field .blank{flex:1;border-bottom:1px solid currentColor;margin-bottom:5px}
  .field .blank--short{flex:0 0 103px}
  .field .suffix{margin-left:8px}
  .card--back-navy .appointment{left:272px;top:32px;color:var(--white)}
  .card--back-white .appointment{left:247px;top:76px;color:var(--ink-dark)}

  .contact-band{position:absolute;left:0;top:228px;width:543px;height:82px;background:var(--red);border-top:3px solid var(--grey-line);color:var(--white);text-align:center;font-family:"Tinos","Times New Roman",serif;font-size:15.5px;line-height:19px;padding-top:5px}
  .contact-band .numbers{margin-top:8px;display:flex;justify-content:center;gap:10px}
  .contact-band .sep{width:1.5px;height:18px;background:var(--white)}
</style>
</head>
<body>
<main class="canvas">

  <section class="card card--front" aria-label="Business card front">
    <svg class="wave" viewBox="0 0 543 310" aria-hidden="true">
      <defs>
        <linearGradient id="redBand" x1="0" x2="1">
          <stop offset="0" stop-color="#6e2a26"/>
          <stop offset=".45" stop-color="#a61d22"/>
          <stop offset="1" stop-color="#b0252a"/>
        </linearGradient>
      </defs>
      <path d="M0,228 C120,278 260,296 543,222 L543,310 L0,310 Z" fill="url(#redBand)"/>
      <path d="M0,224 C120,272 260,290 543,222" fill="none" stroke="#1a3354" stroke-width="7"/>
      <path d="M0,220 C120,266 260,284 543,214" fill="none" stroke="#c9a45c" stroke-width="3"/>
    </svg>
    <div class="guild-mark"><span class="dot"></span>CGFC</div>
    <h1 class="front-text serif doctor-name">Dr. Lumi Harcourt</h1>
    <p class="front-text serif credentials">M.B.B.S., F.C.G.F.C</p>
    <p class="front-text serif role">Family General Practitioner</p>
    <p class="front-text serif address">Upper Level, Lantern Court, Brookvale Arcade Centre<br>Ferncliff, NSW 2190</p>
    <p class="front-text serif phones">
      <span><svg viewBox="0 0 16 16" aria-hidden="true"><path fill="#fff" d="M3.5 1.5l2.5 0 1 3.5-1.7 1.2a8 8 0 0 0 4.5 4.5L11 9l3.5 1v2.5c0 1-1 2-2 2A11 11 0 0 1 1.5 3.5c0-1 1-2 2-2z"/></svg>02 5550 1400</span>
      <span><svg viewBox="0 0 16 16" aria-hidden="true"><path fill="#fff" d="M4 5h8v-3h-8zM2 6h12v6h-2v2h-8v-2h-2zM5 10h6v3h-6z"/></svg>02 5550 1233</span>
    </p>
    <p class="front-text serif tagline">Caring about your health</p>
  </section>

  <section class="card card--back-navy" aria-label="Business card back, navy">
    <span class="guild-ghost" aria-hidden="true">CGFC</span>
    <div class="hours">
      <h2>Working Hours</h2>
      <ul>
        <li>Monday  7 am   - 7 pm</li>
        <li>Tuesday  7 am - 12 pm</li>
        <li>Wednesday  7 am - 10 pm</li>
        <li>Thursday  7 am - 12 pm</li>
        <li>Friday    7 am  - 8 pm</li>
        <li>Saturday  8 am - 10 pm</li>
        <li>Sunday - Off</li>
      </ul>
    </div>
    <span class="divider"></span>
    <div class="appointment">
      <h3>Your Appointment</h3>
      <p class="field">Name<span class="blank"></span></p>
      <p class="field">Date<span class="blank"></span></p>
      <p class="field">Time<span class="blank blank--short"></span><span class="suffix">am/pm</span></p>
    </div>
    <footer class="contact-band">
      <p>Upper Level, Lantern Court, Brookvale Arcade Centre<br>Ferncliff, NSW 2190</p>
      <p class="numbers"><span>P: 02 5550 1400</span><span class="sep"></span><span>F: 02 5550 1233</span></p>
    </footer>
  </section>

  <section class="card card--back-white" aria-label="Business card back, white">
    <span class="guild-ghost" aria-hidden="true">CGFC</span>
    <div class="hours">
      <h2>Working Hours</h2>
      <ul>
        <li>Monday  7 am   - 7 pm</li>
        <li>Tuesday  7 am - 12 pm</li>
        <li>Wednesday  7 am - 10 pm</li>
        <li>Thursday  7 am - 12 pm</li>
        <li>Friday    7 am  - 8 pm</li>
        <li>Saturday  8 am - 10 pm</li>
        <li>Sunday - Off</li>
      </ul>
    </div>
    <span class="divider"></span>
    <div class="appointment">
      <h3>Your Appointment</h3>
      <p class="field">Name<span class="blank"></span></p>
      <p class="field">Date<span class="blank"></span></p>
      <p class="field">Time<span class="blank blank--short"></span><span class="suffix">am/pm</span></p>
    </div>
  </section>

</main>
</body>
</html>
```